“The Future” Spring Fair Poster

We are putting together a school and community fair. We need a poster designed to advertise the event and give some important information to would be attendees. We’d like the poster graphics to evoke a minimalistic and futuristic aesthetic, be bold, yet fun! We will printing the posters, so we will need for them to be at high resolution and ready to send to print.

Target Market(s)

Students, Parents, and Community members

Industry/Entity Type

School

Font styles to use
Sans Serif

Colors
33a6d7
fabb78
9d9d9d
ffffff
1b1b1b
33b8a4

Requirements
Must have
• The Future
• Birch & Harbor Spring Fair 2018
• Friday, May 18th
• 5:00-9:00pm
• Tickets Will Be Available at Select Pick up & Drop Off Times
• Come Enjoy a Futuristic Evening of Food, Music, Entertainment, & Fun!
Nice to have
• We’d love to see a bold and graphic poster with a futuristic feel!
• See the sample image below from previous event poster and additional images for mood and inspiration. Would love to see metallics (silver or metallic colors)

```html
<!DOCTYPE html>
<html lang="en">
<head>
<meta charset="utf-8">
<title>The Future — Birch &amp; Harbor Spring Fair 2018</title>
<link rel="stylesheet" href="https://fonts.googleapis.com/css2?family=Oswald:wght@300;400&family=Open+Sans:wght@400;800&display=swap">
<style>
  :root {
    --navy-deep: #07152b;
    --navy-band: #0f1f38;
    --teal: #33b8a4;
    --silver: #9d9d9d;
    --silver-light: #dfe3e8;
    --white: #ffffff;
    --ribbon-red: #b3201c;
    --frame: rgba(120, 170, 210, 0.45);
  }
  * { box-sizing: border-box; margin: 0; padding: 0; }
  html, body { width: 927px; height: 1200px; overflow: hidden; background: var(--navy-deep); }
  .poster {
    position: relative;
    width: 927px;
    height: 1200px;
    overflow: hidden;
    background:
      radial-gradient(ellipse 60% 40% at 50% 30%, rgba(40, 90, 150, 0.55), transparent 70%),
      radial-gradient(ellipse 80% 60% at 20% 20%, rgba(30, 70, 130, 0.4), transparent 70%),
      linear-gradient(180deg, #0a1a33 0%, #0c2a4c 45%, #0b2342 70%, var(--navy-deep) 100%);
    font-family: "Open Sans", sans-serif;
    color: var(--white);
  }
  .frame {
    position: absolute;
    left: 31px; top: 34px; right: 31px; bottom: 80px;
    border: 1px solid var(--frame);
    pointer-events: none;
  }
  .title {
    position: absolute; left: 0; top: 130px; width: 100%;
    text-align: center;
    font-family: "Oswald", sans-serif; font-weight: 300;
    font-size: 140px; line-height: 1.2;
    color: var(--silver-light);
    text-shadow: 0 4px 6px rgba(0,0,0,0.6);
  }
  .flare {
    position: absolute; left: 213px; top: 300px; width: 500px; height: 40px;
    background: radial-gradient(ellipse 50% 12% at 50% 50%, rgba(255,220,180,0.95), rgba(250,150,80,0.5) 40%, transparent 100%);
  }
  .fair-name {
    position: absolute; left: 0; top: 364px; width: 100%;
    text-align: center;
    font-family: "Oswald", sans-serif; font-weight: 300;
    font-size: 50px; letter-spacing: 0.5px;
    color: var(--white);
    text-shadow: 0 3px 4px rgba(0,0,0,0.8);
  }
  .globe-art {
    position: absolute; left: 163px; top: 440px; width: 600px; height: 410px;
    background:
      radial-gradient(circle at 50% 75%, rgba(180,235,255,0.9) 0%, rgba(70,170,215,0.85) 22%, rgba(25,95,150,0.7) 40%, rgba(20,70,120,0.25) 55%, transparent 66%),
      radial-gradient(ellipse 50% 30% at 50% 100%, rgba(51,184,164,0.55), transparent 80%);
  }
  .ground {
    position: absolute; left: 0; top: 840px; width: 100%; height: 360px;
    background: var(--navy-band);
  }
  .ground svg { position: absolute; left: 0; top: -14px; }
  .details { position: absolute; left: 0; top: 872px; width: 100%; text-align: center; }
  .event-date {
    font-family: "Oswald", sans-serif; font-weight: 400;
    font-size: 48px; line-height: 1.1; color: var(--teal);
  }
  .event-date sup { font-size: 22px; vertical-align: 22px; }
  .event-time {
    font-family: "Oswald", sans-serif; font-weight: 400;
    font-size: 34px; margin-top: 8px; color: var(--white);
  }
  .divider { width: 338px; height: 1px; background: var(--silver); margin: 24px auto 20px; }
  .tickets { font-size: 27px; line-height: 1.25; }
  .tickets strong { display: block; color: var(--teal); font-weight: 800; font-size: 26px; }
  .ribbon { position: absolute; left: 68px; top: 1122px; width: 791px; height: 50px; }
  .ribbon-body {
    position: absolute; left: 14px; right: 14px; top: 0; bottom: 0;
    background: linear-gradient(180deg, #1e3d66 0%, #12294a 100%);
    border: 1px solid rgba(180,210,240,0.6);
    display: flex; align-items: center; justify-content: center;
    font-size: 21.5px; color: var(--white); white-space: nowrap;
  }
  .ribbon svg { position: absolute; top: 0; }
</style>
</head>
<body>
<main class="poster">
  <div class="frame"></div>

  <h1 class="title">The Future</h1>
  <div class="flare"></div>
  <h2 class="fair-name">Birch &amp; Harbor Spring Fair 2018</h2>

  <div class="globe-art" role="img" aria-label="Glowing blue Earth wrapped in a network of connected light points"></div>

  <div class="ground">
    <svg width="927" height="20" viewBox="0 0 927 20" aria-hidden="true">
      <path d="M0 14 L60 12 L120 15 L190 10 L260 13 L330 9 L400 12 L470 8 L540 12 L610 9 L680 13 L750 10 L820 13 L880 11 L927 13 L927 20 L0 20 Z" fill="var(--navy-band)"/>
    </svg>
  </div>

  <section class="details">
    <p class="event-date">Friday, May 18<sup>th</sup></p>
    <p class="event-time">5:00 - 9:00pm</p>
    <div class="divider"></div>
    <p class="tickets">Tickets Will Be Available at<strong>Select Pick up &amp; Drop Off Times</strong></p>
  </section>

  <div class="ribbon">
    <svg class="ribbon-fold-left" style="left:0" width="16" height="18" viewBox="0 0 16 18" aria-hidden="true"><polygon points="16,0 16,18 0,18" fill="var(--ribbon-red)"/></svg>
    <svg class="ribbon-fold-right" style="right:0" width="16" height="18" viewBox="0 0 16 18" aria-hidden="true"><polygon points="0,0 16,18 0,18" fill="var(--ribbon-red)"/></svg>
    <p class="ribbon-body">Come Enjoy a Futuristic Evening of Food, Music, Entertainment, &amp; Fun!</p>
  </div>
</main>
</body>
</html>
```